RZO Design tag

Looking to design a tag for our new hat & glove brand RZO Design. These are winter hats & gloves. Long story short these are lower cost/retail items but I'm trying to convey higher quality goods through a nice tag. I’ve attached a tag of another brand we have to give you a general idea of what I’d be looking for- but again for our new brand RZO Design.
I’m thinking we can do one general design- and then do it in 4 different color schemes: First one mimicking the attachment’s colors for ladies items- so a few different shades of pink. Then 2nd color scheme a darker more masculine color tone for mens or unisex items- maybe blue/dark blue, and then a 3rd color scheme for kids items that is more vibrant/kid like colors. Last one red & green for some Christmas items we do.
A few things:
• Trying to make the tags look classy as possible
• The tag will need to measure 2.25” high x 2” wide. The top little bit would have to be space left blank for a hole punch- just like on the attached sample tag. But again the tags designed would need to be 2.25" tall x 2" wide so not the same shape as the sample tag.
• For item name you can just put “Knit Hat” for the generic tag item name (in place of what says on the same “Chenille Slipper Bootie”). Please try to keep the writing a nice font similar to what is on this tag- again trying to have a classy tag look
• On the bottom center (In place of Made in China) it would just need to say “One Size” in standard font
Hope this helps & thank you
Target Market(s)
People buying winter hats & gloves
Industry/Entity Type
Retail- winter hats & gloves
Look and feel

```html
<!DOCTYPE html>
<html lang="en">
<head>
<meta charset="utf-8">
<title>Knit Hat Tags</title>
<link rel="stylesheet" href="https://fonts.googleapis.com/css2?family=Nanum+Brush+Script&family=Damion&family=Amatic+SC:wght@700&family=Great+Vibes&family=Open+Sans:wght@400&display=swap">
<style>
  :root {
    --page-bg: #f2f2f2;
    --tag-grey: #b3b3b3;
    --ink-white: #ffffff;
    --navy: #21427a;
    --navy-deep: #1b3665;
    --pink: #ff2d82;
    --pink-deep: #c9376f;
    --sun: #ffcc00;
    --sun-deep: #d6ac00;
    --red: #c00000;
    --pine: #1e6539;
    --olive-pill: #7a6a1f;
    --hole-ring: #1a1a1a;
  }
  * { box-sizing: border-box; margin: 0; padding: 0; }
  html, body {
    width: 1092px; height: 1200px; overflow: hidden;
    background: var(--page-bg);
  }
  .sheet { position: relative; width: 1092px; height: 1200px; }

  .tag {
    position: absolute;
    width: 395px; height: 445px;
    background: var(--tag-grey);
    box-shadow: 0 2px 6px rgba(0,0,0,0.3);
    overflow: hidden;
  }
  .tag--men     { left: 131px; top: 112px; }
  .tag--ladies  { left: 563px; top: 112px; }
  .tag--kids    { left: 131px; top: 645px; }
  .tag--holiday { left: 566px; top: 645px; }

  .tag__field {
    position: absolute; left: 0; top: 12px;
    width: 395px; height: 356px;
  }
  .tag--men .tag__field     { background: linear-gradient(135deg, var(--navy) 0%, var(--navy-deep) 50%, var(--navy) 100%); }
  .tag--ladies .tag__field  { background: linear-gradient(135deg, var(--pink) 0%, var(--pink) 40%, var(--pink-deep) 70%, var(--pink) 100%); }
  .tag--kids .tag__field    { background: linear-gradient(135deg, var(--sun) 0%, var(--sun) 40%, var(--sun-deep) 70%, var(--sun) 100%); }
  .tag--holiday .tag__field { background: linear-gradient(135deg, var(--red) 0%, var(--red) 35%, #7a2a1c 60%, var(--red) 100%); }

  .tag__hole {
    position: absolute; left: 181px; top: 11px;
    width: 33px; height: 33px;
  }

  .tag__name { color: var(--ink-white); font-weight: 400; }
  .tag__word {
    position: absolute;
    display: block;
    white-space: nowrap;
    line-height: 1;
    color: var(--ink-white);
  }

  /* Men: tall narrow brush script */
  .tag--men .tag__word {
    font-family: "Nanum Brush Script", cursive;
    font-size: 150px;
    transform: rotate(-6deg);
    transform-origin: left top;
  }
  .tag--men .tag__word--first  { left: 110px; top: 52px; }
  .tag--men .tag__word--second { left: 146px; top: 196px; }

  /* Ladies: upright bold script */
  .tag--ladies .tag__word {
    font-family: "Damion", cursive;
    font-size: 122px;
    transform: rotate(-5deg);
    transform-origin: left top;
  }
  .tag--ladies .tag__word--first  { left: 106px; top: 58px; }
  .tag--ladies .tag__word--second { left: 150px; top: 196px; }

  /* Kids: condensed capitals */
  .tag--kids .tag__word {
    font-family: "Amatic SC", cursive;
    font-weight: 700;
    font-size: 150px;
    transform: rotate(-17deg);
    transform-origin: left top;
  }
  .tag--kids .tag__word--first  { left: 90px; top: 92px; }
  .tag--kids .tag__word--second { left: 150px; top: 240px; }

  /* Holiday: flowing calligraphic script */
  .tag--holiday .tag__word {
    font-family: "Great Vibes", cursive;
    font-size: 128px;
    transform: rotate(-9deg);
    transform-origin: left top;
  }
  .tag--holiday .tag__word--first  { left: 58px; top: 82px; }
  .tag--holiday .tag__word--second { left: 104px; top: 198px; }

  .tag__size {
    position: absolute; left: 50%; top: 407px;
    transform: translate(-50%, -50%);
    padding: 2px 9px 3px;
    border-radius: 11px;
    font-family: "Open Sans", sans-serif;
    font-size: 12.5px;
    line-height: 1.2;
    color: var(--ink-white);
    white-space: nowrap;
  }
  .tag--men .tag__size     { background: var(--navy); }
  .tag--ladies .tag__size  { background: var(--pink-deep); }
  .tag--kids .tag__size    { background: var(--olive-pill); }
  .tag--holiday .tag__size { background: var(--red); }
</style>
</head>
<body>
<main class="sheet">

  <article class="tag tag--men">
    <div class="tag__field" role="img" aria-label="Repeating diagonal letter pattern in navy tones"></div>
    <svg class="tag__hole" viewBox="0 0 33 33" aria-hidden="true">
      <defs><radialGradient id="eyelet-men" cx="45%" cy="40%" r="60%"><stop offset="0" stop-color="#f4f4f4"/><stop offset="1" stop-color="#a8a8a8"/></radialGradient></defs>
      <circle cx="16.5" cy="16.5" r="14.5" fill="url(#eyelet-men)" stroke="var(--hole-ring)" stroke-width="3"/>
    </svg>
    <h2 class="tag__name"><span class="tag__word tag__word--first">Knit</span><span class="tag__word tag__word--second">Hat</span></h2>
    <p class="tag__size">One Size</p>
  </article>

  <article class="tag tag--ladies">
    <div class="tag__field" role="img" aria-label="Repeating diagonal letter pattern in pink tones"></div>
    <svg class="tag__hole" viewBox="0 0 33 33" aria-hidden="true">
      <defs><radialGradient id="eyelet-ladies" cx="45%" cy="40%" r="60%"><stop offset="0" stop-color="#f4f4f4"/><stop offset="1" stop-color="#a8a8a8"/></radialGradient></defs>
      <circle cx="16.5" cy="16.5" r="14.5" fill="url(#eyelet-ladies)" stroke="var(--hole-ring)" stroke-width="3"/>
    </svg>
    <h2 class="tag__name"><span class="tag__word tag__word--first">Knit</span><span class="tag__word tag__word--second">Hat</span></h2>
    <p class="tag__size">One Size</p>
  </article>

  <article class="tag tag--kids">
    <div class="tag__field" role="img" aria-label="Repeating diagonal letter pattern in yellow tones"></div>
    <svg class="tag__hole" viewBox="0 0 33 33" aria-hidden="true">
      <defs><radialGradient id="eyelet-kids" cx="45%" cy="40%" r="60%"><stop offset="0" stop-color="#f4f4f4"/><stop offset="1" stop-color="#a8a8a8"/></radialGradient></defs>
      <circle cx="16.5" cy="16.5" r="14.5" fill="url(#eyelet-kids)" stroke="var(--hole-ring)" stroke-width="3"/>
    </svg>
    <h2 class="tag__name"><span class="tag__word tag__word--first">Knit</span><span class="tag__word tag__word--second">Hat</span></h2>
    <p class="tag__size">One Size</p>
  </article>

  <article class="tag tag--holiday">
    <div class="tag__field" role="img" aria-label="Repeating diagonal letter pattern in red and green"></div>
    <svg class="tag__hole" viewBox="0 0 33 33" aria-hidden="true">
      <defs><radialGradient id="eyelet-holiday" cx="45%" cy="40%" r="60%"><stop offset="0" stop-color="#f4f4f4"/><stop offset="1" stop-color="#a8a8a8"/></radialGradient></defs>
      <circle cx="16.5" cy="16.5" r="14.5" fill="url(#eyelet-holiday)" stroke="var(--hole-ring)" stroke-width="3"/>
    </svg>
    <h2 class="tag__name"><span class="tag__word tag__word--first">Knit</span><span class="tag__word tag__word--second">Hat</span></h2>
    <p class="tag__size">One Size</p>
  </article>

</main>
</body>
</html>
```